Zielgruppe
Wir sind ein Hotelunternehmen und eröffnen einen neuen Standort mit einem Boutique-Hotel. Die Zielgruppe sind Hotelgäste.
Aufgabenstellung
Wir benötigen ein Plakat mit den Maßen 6x4 m (siehe Bild anbei) für unsseren neuen Standort.
Farben Schwarz Weiss
Das Haus wird noch komplett weiß eingekleidet für die spätere Enthüllung und dann kommt das Plakat drüber
TEXT:
Großes Logo Hotel
Wir machen Lustenau noch schöner
Hier entsteht unser Boutique Hotel
Aus der Firmengruppe der Tarvolenz (als Logo)
Bild von Lena Grubhofer mit dem untertext: Lena Grubhofer, Geschäftsführerin Business Hotel Grubhofer

```html
<!DOCTYPE html>
<html lang="de">
<head>
<meta charset="utf-8">
<title>Grubhofer Boutique Hotel – Plakat</title>
<link href="https://fonts.googleapis.com/css2?family=Montserrat:wght@400;600&display=swap" rel="stylesheet">
<style>
  :root {
    --paper: #ffffff;
    --panel-light: #b0b0b0;
    --panel-dark: #474747;
    --text-light: #ffffff;
    --text-muted: #9d9d9d;
    --portrait-top: #e9e9e9;
    --portrait-bottom: #cfcfcf;
  }
  html, body {
    margin: 0;
    padding: 0;
    overflow: hidden;
    background: var(--paper);
  }
  .poster {
    position: relative;
    width: 1200px;
    height: 800px;
    background: var(--paper);
    overflow: hidden;
    font-family: "Montserrat", sans-serif;
  }
  .panel-light {
    position: absolute;
    left: 20px; top: 20px;
    width: 402px; height: 760px;
    background: var(--panel-light);
  }
  .panel-dark {
    position: absolute;
    left: 422px; top: 20px;
    width: 758px; height: 760px;
    background: var(--panel-dark);
  }
  .portrait {
    position: absolute;
    left: 0; top: 92px;
    width: 450px; height: 688px;
    border-radius: 160px 160px 0 0;
    background: linear-gradient(180deg, var(--portrait-top), var(--portrait-bottom));
  }
  .hotel-name {
    position: absolute;
    left: 532px; top: 232px;
    width: 510px;
    margin: 0;
    text-align: center;
    color: var(--text-light);
    font-weight: 600;
    font-size: 84px;
    line-height: 1;
    letter-spacing: 1px;
  }
  .hotel-type {
    position: absolute;
    left: 597px; top: 378px;
    margin: 0;
    color: var(--text-light);
    font-weight: 600;
    font-size: 33px;
    letter-spacing: 8px;
    line-height: 1;
  }
  .message {
    position: absolute;
    left: 596px; top: 480px;
    margin: 0;
    color: var(--text-light);
    font-weight: 400;
    font-size: 26px;
    line-height: 34px;
    letter-spacing: 0.5px;
  }
  .message p { margin: 0; }
  .message .tagline { margin-bottom: 34px; }
  .group-name {
    display: flex;
    align-items: center;
    gap: 6px;
    margin-top: 4px;
    color: var(--text-light);
    font-weight: 600;
    font-size: 24px;
  }
  .group-dot {
    width: 9px; height: 9px;
    border-radius: 50%;
    background: var(--text-light);
  }
  .signature {
    position: absolute;
    left: 458px; top: 730px;
    margin: 0;
    color: var(--text-muted);
    font-size: 16px;
    letter-spacing: 2.4px;
    white-space: nowrap;
  }
  .signature .sep { margin: 0 16px; }
</style>
</head>
<body>
  <main class="poster">
    <div class="panel-light"></div>
    <div class="panel-dark"></div>
    <div class="portrait" role="img" aria-label="Porträtfoto von Lena Grubhofer in weißer Bluse"></div>

    <h1 class="hotel-name">Grubhofer</h1>
    <p class="hotel-type">BOUTIQUE HOTEL</p>

    <section class="message">
      <p class="tagline">Wir machen Lustenau noch schöner.</p>
      <p>Hier entsteht unser Boutique Hotel<br>aus der Firmengruppe der</p>
      <div class="group-name">Tarvolenz<span class="group-dot"></span></div>
    </section>

    <p class="signature">Lena Grubhofer<span class="sep">·</span>Geschäftsführerin<span class="sep">·</span>Business Hotel Grubhofer</p>
  </main>
</body>
</html>
```